Corvantis websites redesign

Www.cor-vantis.com needs to be redesigned along with updations. The incremental material will be provided for the updations. We are looking for complete redesign of the pages with the new content. The complete write up will be provided soon

Target Market(s)

Global

Coding

Coded - Design and coding required

Number of Pages Required

5+ page

Requirements
Must have
• A clean and slick design for the Consulting.
Should not have
• Too many pictures which reduces the speed of the site

```html
<!DOCTYPE html>
<html lang="en">
<head>
<meta charset="utf-8">
<title>Corvantis – Consultancy</title>
<link href="https://fonts.googleapis.com/css2?family=Lato:wght@300;400;700&family=Arimo:wght@400;700&display=swap" rel="stylesheet">
<style>
:root{
  --accent:#1e9ad6;
  --ink:#444;
  --body:#555;
  --muted:#666;
  --rule:#cfcfcf;
  --footer-bg:#1b1b1b;
  --footer-text:#9b9b9b;
  --footer-head:#e6e6e6;
  --white:#fff;
}
*{margin:0;padding:0;box-sizing:border-box}
html,body{width:1078px;height:1200px;overflow:hidden;background:var(--white)}
body{position:relative;font-family:"Arimo",Arial,sans-serif;color:var(--body)}
.abs{position:absolute}

/* header */
.site-header{position:absolute;left:0;top:0;width:1078px;height:56px;border-bottom:1px solid #e4e4e4}
.brand{position:absolute;left:243px;top:16px;display:flex;align-items:center;gap:8px;font-family:"Lato",sans-serif;font-weight:400;font-size:21px;color:#2b3a55}
.brand-dot{width:18px;height:18px;border-radius:50%;background:#2b3a55}
.main-nav a{position:absolute;top:25px;font-family:"Lato",sans-serif;font-size:9.5px;color:#666;text-decoration:none;transform:translateX(-50%);white-space:nowrap}
.main-nav a.is-active{color:var(--accent)}
.nav-underline{position:absolute;left:610px;top:53px;width:44px;height:2px;background:var(--accent)}

/* content */
.section-title{position:absolute;font-family:"Lato",sans-serif;font-weight:400;font-size:13.5px;color:var(--ink);white-space:nowrap}
.copy{position:absolute;font-size:7.6px;line-height:12px;color:#444}
.copy p+p{margin-top:12px}
.copy .lead-link{color:var(--accent)}
.expertise{position:absolute;list-style:none;font-size:7.6px;line-height:12px;color:var(--muted)}
.expertise li{position:relative;padding-left:12px}
.expertise li::before{content:"»";position:absolute;left:0;top:0;color:#999}
.divider{position:absolute;left:243px;width:593px;height:1px;background:var(--rule)}
.media{position:absolute}

/* footer */
.site-footer{position:absolute;left:0;top:958px;width:1078px;height:242px;background:var(--footer-bg);color:var(--footer-text)}
.footer-brand{position:absolute;left:243px;top:42px;display:flex;align-items:center;gap:7px;font-family:"Lato",sans-serif;font-size:15px;color:#a8a8a8}
.footer-brand .brand-dot{width:15px;height:15px;background:#8a8a8a}
.address{position:absolute;left:245px;top:78px;font-size:7.6px;line-height:13px}
.contact-line{position:absolute;left:245px;font-size:7.6px}
.contact-line strong{color:var(--accent);font-size:8.8px}
.contact-line a{color:var(--accent)}
.footer-head{position:absolute;top:50px;font-family:"Lato",sans-serif;font-size:9.5px;color:var(--footer-head);letter-spacing:.2px}
.footer-head::after{content:"";position:absolute;left:0;top:15px;width:19px;height:1px;background:#bbb}
.footer-note{position:absolute;left:434px;top:80px;font-size:7.6px}
.subscribe{position:absolute;left:434px;top:99px;width:135px;height:24px;border:1px solid #555;font-size:7.6px;color:#bbb;padding:7px 0 0 9px}
.subscribe svg{position:absolute;right:7px;top:7px}
.site-links{position:absolute;left:626px;top:78px;list-style:none;font-size:7.6px;line-height:16px}
.site-links li{padding-left:11px;position:relative;color:#bbb}
.site-links li::before{content:"»";position:absolute;left:0;color:#888}
.site-links li.is-active{color:var(--accent);text-decoration:underline}
.social{position:absolute;left:750px;top:79px;display:flex;gap:2px}
.social span{width:20px;height:20px;border-radius:50%;border:1.2px solid #bbb}
.social span.is-first{border-color:var(--accent)}
.footer-bar{position:absolute;left:0;top:203px;width:1078px;height:1px;background:#2e2e2e}
.copyright{position:absolute;left:243px;top:218px;font-size:7.6px}
</style>
</head>
<body>

<header class="site-header">
  <div class="brand"><span class="brand-dot"></span>Corvantis</div>
  <nav class="main-nav">
    <a style="left:521px">Home</a>
    <a style="left:574px">Founder</a>
    <a style="left:632px" class="is-active">Consultancy</a>
    <a style="left:692px">Platform</a>
    <a style="left:750px">Case Studies</a>
    <a style="left:814px">Contact Us</a>
  </nav>
  <div class="nav-underline"></div>
</header>

<!-- Bank consultancy -->
<div class="media" role="img" aria-label="Photo of three people reviewing documents at a desk" style="left:243px;top:110px;width:216px;height:125px;background:linear-gradient(120deg,#d9dbde 0%,#bfc3c8 40%,#e8e4df 65%,#5b9ad8 100%)"></div>
<h2 class="section-title" style="left:487px;top:105px">Bank Consultancy</h2>
<div class="copy" style="left:488px;top:140px;width:348px">
  <p>Capacity Building for Trade Finance either through Export Credit Insurance/ Developmental Financial Institution and Private Risk Insurance from a Risk and Marketing Perspective.</p>
  <p>Arrangement of Long term liability from alternate sources of liquidity for onlending purposes to emerging country banks.</p>
</div>
<div class="divider" style="top:270px"></div>

<!-- Plain vanilla -->
<h2 class="section-title" style="left:243px;top:306px">Corporate Consultancy - Plain Vanilla Financing</h2>
<div class="copy" style="left:243px;top:344px;width:345px;line-height:12.9px">
  <p>The Consultancy provides access to local/regional banks across Hong Kong, Singapore, Dubai , New York and London and helps corporate clients in diversifying their financial partners and adding new banks to their bank group. The Consultancy provides Trade finance solutions for working capital requirements and assists in arranging External Commercial Borrowings/Foreign Currency Term Loans for long-term requirements. <span class="lead-link">Our main areas of expertise:</span></p>
</div>
<ul class="expertise" style="left:243px;top:425px;width:360px">
  <li style="margin-bottom:9.5px">Introduction of regional bank for Subsidiaries /Joint Ventures across the world</li>
  <li style="margin-bottom:9.5px">Plain-vanilla working capital lines from banks – Letter of Credit, Trust Receipt, Bill Discounting, etc</li>
  <li style="margin-bottom:9.5px">Arranging External Commercial Borrowings/Foreign Currency Term Loans for long-term requirement</li>
  <li style="margin-bottom:9.5px">Providing efficiency in terms of better leverage and pricing through new lenders</li>
  <li>Bank line business like Guarantee issuance and LC confirmations over longer tenor</li>
</ul>
<div class="media" role="img" aria-label="Photo of reading glasses and a pen resting on printed financial charts" style="left:620px;top:310px;width:216px;height:125px;background:linear-gradient(135deg,#b9803f 0%,#3b3b40 30%,#eef2f7 55%,#9cc0e6 80%,#f4f6f9 100%)"></div>
<div class="divider" style="top:561px"></div>

<!-- Structured -->
<div class="media" role="img" aria-label="Photo of a keyboard with a solution key beside a globe" style="left:243px;top:608px;width:216px;height:124px;background:linear-gradient(120deg,#c4d6ea 0%,#9db9da 45%,#e6edf5 70%,#2f5f93 100%)"></div>
<h2 class="section-title" style="left:487px;top:602px">Corporate Consultancy - Structured Financing Solutions</h2>
<div class="copy" style="left:488px;top:638px;width:348px">
  <p>The Consultancy provides end-to-end structured solutions on the Payables, Receivables or Inventory side for working capital requirements with off/part/on recourse balance sheet structures. We also specialize in providing credit enhancements through private or sovereign Insurance market to enhance the rating of a debt paper and improve distribution and market appetite.</p>
  <p>On the term side, the Consultancy focuses on providing access to alternate liquidity providers like Developmental Financial Institutions, Export Credit Agency and Hedge Funds for both corporates and banks<br>The Consultancy through varied structure can also assist in monetization of unfunded bank lines for arranging financing. <span class="lead-link">The following are our main areas of expertise:</span></p>
</div>
<ul class="expertise" style="left:488px;top:778px;width:348px">
  <li style="margin-bottom:10px">Structured working capital solutions – like back-to-back LC, front-to-back LC, etc.</li>
  <li style="margin-bottom:11px">Export prepayments - Pre-export unsecured advance against contracts/open account/LC with the Buyers. This significantly reduces the working capital utilisation of most companies</li>
  <li style="margin-bottom:14px">Structured project financing through Export Credit Agencies and Developmental Financial Institutions - Direct credit limit on the projects can be looked into either with a single DFI or with a consortium of ECA/DFI's which makes the project significantly scalable</li>
  <li>Recourse/ part recourse/ non-recourse receivables financing – with or without credit enhancements</li>
</ul>

<footer class="site-footer">
  <div class="footer-brand"><span class="brand-dot"></span>Corvantis</div>
  <div class="address">Corvantis Consultancy Ltd<br>Unit 04, 9th Floor, Harbour Crest Tower,<br>18 Lantern Quay Road, Kowloon<br>Hong Kong</div>
  <div class="contact-line" style="top:143px">T: <strong>852-310 55218</strong></div>
  <div class="contact-line" style="top:158px">E: <a>query@cor-vantis.com</a></div>

  <h3 class="footer-head" style="left:434px">GET IN TOUCH!</h3>
  <div class="footer-note">Simply Drop Your Mail Here</div>
  <div class="subscribe">Your Email Here
    <svg width="11" height="8" viewBox="0 0 11 8"><rect x="0.5" y="0.5" width="10" height="7" fill="none" stroke="#1e9ad6"/><path d="M0.5 0.5 L5.5 4.5 L10.5 0.5" fill="none" stroke="#1e9ad6"/></svg>
  </div>

  <h3 class="footer-head" style="left:626px">SITE LINKS</h3>
  <ul class="site-links">
    <li>Home</li><li>Founder</li><li class="is-active">Consultancy</li><li>Platform</li><li>Case Studies</li><li>Contact Us</li>
  </ul>

  <h3 class="footer-head" style="left:750px">SOCIAL LINKS</h3>
  <div class="social"><span class="is-first"></span><span></span><span></span><span></span></div>

  <div class="footer-bar"></div>
  <div class="copyright">© 2016 Corvantis Consultancy Limited</div>
</footer>

</body>
</html>
```